Harlow Inquiry Partners PLLC
Law Firm Conducting Investigations
Harlow Inquiry Partners PLLC -
Creative Brief
Professional
Dale Morrow
Attorney
21430 SW 3rd Ave, Suite C2-418 Bellevue, WA 98006
dale@harlowinquiry-example.com
www.harlowinquiry-example.com
I would like the card to be simple, clean and professional. Please use color schemes that match the logo, but don't use too much gold.
The back of the card should be blank.

```html
<!DOCTYPE html>
<html lang="en">
<head>
<meta charset="utf-8">
<title>Harlow Inquiry Partners PLLC – Business Card</title>
<link rel="stylesheet" href="https://fonts.googleapis.com/css2?family=Tinos:wght@400;700&display=swap">
<style>
  :root {
    --page-bg: #e9e9ea;
    --card-black: #0b0b0b;
    --gold: #b08f3a;
    --text-white: #ffffff;
    --text-cream: #f1ead6;
  }
  html, body {
    margin: 0;
    padding: 0;
    width: 1200px;
    height: 946px;
    overflow: hidden;
    background: var(--page-bg);
  }
  .business-card {
    position: absolute;
    left: 50px;
    top: 158px;
    width: 1100px;
    height: 630px;
    background: var(--card-black);
    overflow: hidden;
    font-family: "Tinos", "Times New Roman", serif;
    color: var(--text-white);
  }
  .card-art {
    position: absolute;
    inset: 0;
  }
  .brand {
    position: absolute;
    left: 40px;
    top: 70px;
    display: flex;
    align-items: center;
    gap: 26px;
  }
  .brand-mark {
    width: 70px;
    height: 70px;
    background: var(--gold);
  }
  .brand-name {
    font-weight: 400;
    font-size: 40px;
    line-height: 1.1;
    color: var(--gold);
  }
  .contact {
    position: absolute;
    left: 20px;
    top: 322px;
    font-size: 36px;
    line-height: 50px;
    white-space: nowrap;
  }
  .contact p { margin: 0; }
  .contact .gap { margin-top: 8px; }
  .person {
    position: absolute;
    left: 790px;
    top: 392px;
    white-space: nowrap;
  }
  .person-name {
    font-weight: 700;
    font-size: 46px;
    line-height: 1;
  }
  .person-title {
    font-size: 38px;
    margin-top: 10px;
    color: var(--text-cream);
  }
</style>
</head>
<body>
  <div class="business-card">
    <svg class="card-art" width="1100" height="630" viewBox="0 0 1100 630" aria-hidden="true">
      <defs>
        <linearGradient id="rule-gold" x1="0" x2="1" y1="0" y2="0">
          <stop offset="0" stop-color="#d8b85a" stop-opacity="0.9"/>
          <stop offset="0.75" stop-color="#a8862f"/>
          <stop offset="1" stop-color="#a8862f" stop-opacity="0"/>
        </linearGradient>
        <linearGradient id="panel-gold" x1="0" x2="1" y1="0" y2="1">
          <stop offset="0" stop-color="#c9a445"/>
          <stop offset="0.5" stop-color="#9a7a2a"/>
          <stop offset="1" stop-color="#5e4714"/>
        </linearGradient>
        <linearGradient id="frame-silver" x1="0" x2="1" y1="0" y2="1">
          <stop offset="0" stop-color="#f4f4f4"/>
          <stop offset="1" stop-color="#9a9a9a"/>
        </linearGradient>
      </defs>
      <rect class="gold-rule" x="0" y="238" width="1160" height="6" fill="url(#rule-gold)"/>
      <polygon class="diamond-frame" points="915,70 1230,385 915,700 600,385" fill="url(#frame-silver)"/>
      <polygon class="diamond-inner-black" points="915,92 1208,385 915,678 622,385" fill="#0b0b0b"/>
      <polygon class="diamond-panel" points="915,110 1190,385 915,660 640,385" fill="url(#panel-gold)"/>
    </svg>

    <div class="brand">
      <div class="brand-mark"></div>
      <div class="brand-name">Harlow Inquiry<br>Partners</div>
    </div>

    <div class="contact">
      <p>21430 SW 3rd Ave, Suite C2-418</p>
      <p>Bellevue, WA 98006</p>
      <p class="gap">phone: 425-555-0147</p>
      <p>dale@harlowinquiry-example.com</p>
      <p>www.harlowinquiry-example.com</p>
    </div>

    <div class="person">
      <div class="person-name">Dale Morrow</div>
      <div class="person-title">Attorney</div>
    </div>
  </div>
</body>
</html>
```